IT COMPANYcutting edge tec business card

we are IT company that building any apps.
we need business card in japanese and english
You don’t have to include all information in front one you can attach part of that information to back-side
company name : 株式会社ひかりの丘 (BRIGHTHILL Inc.)
concept : cutting-edge technology
role : 取締役 (director)
name : 呉 炫秀 (Oh Hyeonsuk)
post number : 154-0038
address : 東京都世田谷区西若葉台5-14-8 (5-14-8, Nishiwakabadai, Setagaya Ku, Tokyo To, 154-0038, Japan)
Tel:+81-3-5917-2846
Mobile:+81-80-7253-3169
Email : hoh@brighthill-lab.com
website : www.brighthill-lab.com

we dont have logo so please make it as well
we also looking for designer who can make homapage design.

Contact Information for Business Card

cutting-edge design and modern for IT

Font styles to use
Sans Serif

Colors
34a6d7
33b8a4
6092c4
3377b5
886aae
6b449b
b868aa
a64599

Requirements
Must have
• Simple but designed

```html
<!DOCTYPE html>
<html lang="ja">
<head>
<meta charset="utf-8">
<title>BRIGHTHILL Inc. — Business Card</title>
<link rel="stylesheet" href="https://fonts.googleapis.com/css2?family=Inter:wght@400;500;600&family=Noto+Sans+JP:wght@400;500;600&display=swap">
<style>
  :root {
    --bg: #e6eaee;
    --card-white: #f7f8f9;
    --ink: #1d1f22;
    --ink-soft: #3a3d42;
    --brand-blue: #0a96e6;
    --grad-start: #0b95ea;
    --grad-end: #00dcd8;
    --white: #ffffff;
  }
  * { box-sizing: border-box; margin: 0; padding: 0; }
  html, body {
    width: 1200px;
    height: 787px;
    overflow: hidden;
  }
  body {
    background: var(--bg);
    font-family: "Inter", "Noto Sans JP", Arial, sans-serif;
    color: var(--ink);
    position: relative;
  }
  .jp { font-family: "Noto Sans JP", "Inter", sans-serif; }

  .card {
    position: absolute;
    top: 240px;
    width: 500px;
    height: 304px;
    border-radius: 16px;
    box-shadow: 0 10px 28px rgba(20, 40, 60, 0.18);
    overflow: hidden;
  }
  .card--front {
    left: 70px;
    background: var(--card-white);
  }
  .card--back {
    left: 630px;
    background: linear-gradient(135deg, var(--grad-start) 0%, var(--grad-end) 100%);
    display: flex;
    align-items: center;
    justify-content: center;
  }

  /* Brand name */
  .brand {
    display: flex;
    align-items: center;
    gap: 10px;
  }
  .brand__mark {
    width: 22px;
    height: 22px;
    background: var(--brand-blue);
    border-radius: 4px;
  }
  .brand__name {
    font-weight: 500;
    font-size: 22px;
    letter-spacing: 0.02em;
    color: var(--ink);
  }
  .card--front .brand {
    position: absolute;
    left: 40px;
    top: 34px;
  }
  .company-jp {
    position: absolute;
    left: 72px;
    top: 64px;
    font-size: 11px;
    font-weight: 500;
    letter-spacing: 0.08em;
    color: var(--ink-soft);
  }
  .brand--reverse .brand__mark { background: var(--white); width: 34px; height: 34px; border-radius: 6px; }
  .brand--reverse .brand__name { color: var(--white); font-size: 34px; font-weight: 600; }

  /* Address */
  .address {
    position: absolute;
    left: 40px;
    top: 118px;
    font-style: normal;
    font-size: 10.5px;
    line-height: 1.6;
    letter-spacing: 0.02em;
    text-transform: uppercase;
    color: var(--ink-soft);
  }
  .address__jp {
    display: block;
    margin-bottom: 3px;
    letter-spacing: 0.04em;
  }

  /* Person */
  .person {
    position: absolute;
    left: 300px;
    top: 114px;
  }
  .person__jp {
    display: flex;
    align-items: baseline;
    gap: 8px;
  }
  .person__name-jp {
    font-size: 17px;
    font-weight: 600;
    letter-spacing: 0.12em;
    color: var(--ink);
  }
  .person__role-jp {
    font-size: 10.5px;
    color: var(--ink-soft);
    letter-spacing: 0.06em;
  }
  .person__name {
    margin-top: 4px;
    font-size: 15px;
    font-weight: 600;
    letter-spacing: 0.03em;
    color: var(--brand-blue);
    text-transform: uppercase;
  }
  .person__role {
    margin-top: 2px;
    font-size: 10.5px;
    letter-spacing: 0.04em;
    text-transform: uppercase;
    color: var(--ink-soft);
  }

  /* Contacts */
  .contacts {
    position: absolute;
    left: 210px;
    bottom: 28px;
    list-style: none;
    font-size: 11px;
    letter-spacing: 0.02em;
    text-transform: uppercase;
    color: var(--ink-soft);
  }
  .contacts__item {
    display: flex;
    align-items: center;
    gap: 8px;
    line-height: 1.7;
  }
  .contacts__icon {
    width: 11px;
    height: 11px;
    flex: none;
    fill: none;
    stroke: var(--brand-blue);
    stroke-width: 1.6;
  }
  .contacts__icon--solid { fill: var(--brand-blue); stroke: none; }
</style>
</head>
<body>

  <section class="card card--front" aria-label="Business card front">
    <div class="brand">
      <span class="brand__mark"></span>
      <span class="brand__name">BRIGHTHILL</span>
    </div>
    <p class="company-jp jp">株式会社ひかりの丘</p>

    <address class="address">
      <span class="address__jp jp">〒154-0038<br>東京都世田谷区西若葉台5-14-8</span>
      5-14-8, Nishiwakabadai<br>
      Setagaya Ku, Tokyo To<br>
      154-0038, Japan
    </address>

    <div class="person">
      <p class="person__jp jp">
        <span class="person__role-jp">取締役</span>
        <span class="person__name-jp">呉 炫秀</span>
      </p>
      <p class="person__name">Oh Hyeonsuk</p>
      <p class="person__role">Director</p>
    </div>

    <ul class="contacts">
      <li class="contacts__item">
        <svg class="contacts__icon contacts__icon--solid" viewBox="0 0 12 12" aria-hidden="true">
          <path d="M2.2 0.8l2 0.2 0.8 2.4-1.2 1a7 7 0 0 0 3.8 3.8l1-1.2 2.4 0.8 0.2 2-1.4 1.2C5 10.8 1.2 7 0.8 2.2z"/>
        </svg>
        <span>+81-3-5917-2846</span>
      </li>
      <li class="contacts__item">
        <svg class="contacts__icon" viewBox="0 0 12 12" aria-hidden="true">
          <rect x="3" y="0.8" width="6" height="10.4" rx="1"/>
          <line x1="5" y1="9.3" x2="7" y2="9.3"/>
        </svg>
        <span>+81-80-7253-3169</span>
      </li>
      <li class="contacts__item">
        <svg class="contacts__icon" viewBox="0 0 12 12" aria-hidden="true">
          <rect x="0.8" y="2.5" width="10.4" height="7" rx="0.6"/>
          <polyline points="0.8,2.8 6,6.6 11.2,2.8"/>
        </svg>
        <span>hoh@brighthill-lab.com</span>
      </li>
      <li class="contacts__item">
        <svg class="contacts__icon" viewBox="0 0 12 12" aria-hidden="true">
          <circle cx="6" cy="6" r="5.2"/>
          <ellipse cx="6" cy="6" rx="2.3" ry="5.2"/>
          <line x1="0.8" y1="6" x2="11.2" y2="6"/>
        </svg>
        <span>www.brighthill-lab.com</span>
      </li>
    </ul>
  </section>

  <section class="card card--back" aria-label="Business card back">
    <div class="brand brand--reverse">
      <span class="brand__mark"></span>
      <span class="brand__name">BRIGHTHILL</span>
    </div>
  </section>

</body>
</html>
```